Verdant Loop Advisors, LLC

I am looking for a simple, clear layout with my logo prominent and embossed, on the best quality card stock available. I would like the business name and phone number included on the card as well......I dont want my name anywhere on the card and I would like my logo embossed on the card......something simple with a white back......open to designs as long as they go along with recycling symbols and green type stuff.....The address, website, cell number, fax number, and email are listed below

5374 Tillbury Fenwood Road
Hyattsville, MD 20785

c. 240.555.0143 f. 240.555.0187
e. sales@verdantloopadvisors.example
w. www.verdantloopadvisors.example

Industry/Entity Type

Recycling

```html
<!DOCTYPE html>
<html lang="en">
<head>
<meta charset="utf-8">
<title>Verdant Loop Advisors, LLC — Business Card</title>
<link rel="stylesheet" href="https://fonts.googleapis.com/css2?family=Montserrat:wght@500;600;700&display=swap">
<style>
  :root {
    --page: #e9e7e4;
    --card: #ffffff;
    --card-shade: #ececec;
    --band: #2e2925;
    --green: #2f7a4a;
    --green-light: #5aa06f;
    --ink: #2b2724;
    --ink-soft: #5c5752;
    --white: #ffffff;
  }
  * { margin: 0; padding: 0; box-sizing: border-box; }
  html, body {
    width: 1200px;
    height: 899px;
    overflow: hidden;
    background: var(--page);
    font-family: "Montserrat", Arial, sans-serif;
  }
  .canvas {
    position: relative;
    width: 1200px;
    height: 899px;
  }
  .business-card {
    position: absolute;
    left: 150px;
    top: 192px;
    width: 900px;
    height: 515px;
    border-radius: 44px;
    overflow: hidden;
    background: radial-gradient(ellipse at 40% 60%, var(--card) 45%, var(--card-shade) 100%);
    box-shadow: 0 18px 40px rgba(0,0,0,0.18);
  }
  .card-band {
    position: absolute;
    inset: 0;
    width: 900px;
    height: 515px;
  }
  .address {
    position: absolute;
    left: 48px;
    top: 244px;
    font-size: 16px;
    font-style: normal;
    font-weight: 500;
    line-height: 24px;
    color: var(--ink);
  }
  .contact-list {
    position: absolute;
    left: 48px;
    top: 316px;
    list-style: none;
  }
  .contact-item {
    display: flex;
    align-items: center;
    gap: 12px;
    height: 28px;
    font-size: 14px;
    font-weight: 500;
    color: var(--ink-soft);
  }
  .contact-icon {
    width: 14px;
    height: 14px;
    flex: none;
  }
  .brand {
    position: absolute;
    right: 52px;
    bottom: 52px;
    display: flex;
    align-items: center;
    gap: 18px;
  }
  .brand-mark {
    width: 58px;
    height: 58px;
    background: var(--green);
    flex: none;
  }
  .brand-name {
    font-size: 34px;
    font-weight: 700;
    line-height: 40px;
    letter-spacing: 1px;
    color: var(--ink);
    text-transform: uppercase;
  }
</style>
</head>
<body>
<main class="canvas">
  <section class="business-card" aria-label="Verdant Loop Advisors business card">
    <svg class="card-band" viewBox="0 0 900 515" aria-hidden="true">
      <path d="M0 0 H900 V118 C760 112 640 150 470 176 C300 200 150 170 0 196 Z" fill="var(--band)"/>
      <path d="M0 208 C150 182 300 212 470 188 C640 162 760 126 900 130" fill="none" stroke="var(--green)" stroke-width="5"/>
      <path d="M0 220 C160 196 320 222 480 198 C650 172 770 140 900 144" fill="none" stroke="var(--green-light)" stroke-width="2"/>
    </svg>

    <address class="address">
      5374 Tillbury Fenwood Road<br>
      Hyattsville, MD 20785
    </address>

    <ul class="contact-list">
      <li class="contact-item">
        <svg class="contact-icon" viewBox="0 0 14 14" aria-hidden="true"><path d="M3 1 L5 1 L6 4 L4.5 5.2 C5.3 7 7 8.7 8.8 9.5 L10 8 L13 9 L13 11 C13 12 12 13 11 13 C5.5 12.6 1.4 8.5 1 3 C1 2 2 1 3 1 Z" fill="var(--green)"/></svg>
        240.555.0143
      </li>
      <li class="contact-item">
        <svg class="contact-icon" viewBox="0 0 14 14" aria-hidden="true"><rect x="1" y="5" width="12" height="7" rx="1" fill="var(--green)"/><rect x="3.5" y="1" width="7" height="5" fill="var(--green)"/><rect x="4.5" y="2" width="5" height="3" fill="var(--white)"/></svg>
        240.555.0187
      </li>
      <li class="contact-item">
        <svg class="contact-icon" viewBox="0 0 14 14" aria-hidden="true"><rect x="1" y="3" width="12" height="8.5" rx="1" fill="var(--green)"/><path d="M1.5 3.5 L7 8 L12.5 3.5" fill="none" stroke="var(--white)" stroke-width="1.2"/></svg>
        sales@verdantloopadvisors.example
      </li>
      <li class="contact-item">
        <svg class="contact-icon" viewBox="0 0 14 14" aria-hidden="true"><circle cx="7" cy="7" r="6" fill="var(--green)"/><ellipse cx="7" cy="7" rx="2.6" ry="6" fill="none" stroke="var(--white)" stroke-width="1"/><line x1="1" y1="7" x2="13" y2="7" stroke="var(--white)" stroke-width="1"/></svg>
        www.verdantloopadvisors.example
      </li>
    </ul>

    <div class="brand">
      <span class="brand-mark" aria-hidden="true"></span>
      <p class="brand-name">Verdant Loop<br>Advisors, LLC</p>
    </div>
  </section>
</main>
</body>
</html>
```